International oil and gas consultancy business needs a web design

Hello, I need a web design for a new oil and gas auditing consultancy business. My business undertakes contract audit assignments to review past costs of oil and gas operations (see attached Excel file for more details of the businesses services). I need the design to give the impression of a professional consultancy style of business, rather than a retail style of website. Note: this job is for LAYOUT DESIGN ONLY and not coding / development work.
The following are my key design principles:
1. BASIC DESIGN: I am after a simple and static web design. I don't want the pages busy or cluttered with too many images or detail.
2. HORIZONTAL TABS: I require a horizontal set of tabs towards the top of the screens (see Excel file) which remain in the same position on every page.
3. META TAG PLANNING: The design should allow for effective positioning of content so that key meta tag words can easily be built during the technical build stage.
4. NUMBER OF PAGES: The site will eventually have a maximum of 10 pages. Seven of the pages will reside under the tabs. Can you please present your opening submission for the first two page.
5. USE OF MY LOGO: The attached logo (JPEG file) should be used throughout the website. Please don't change the shape and colour.
6. COLOUR SCHEMES: Can you please consider any of the 3 colour schemes below:
A - dark red (to match the logo), light grey and perhaps another of your liking;
B - dark red (to match the logo), light cream and perhaps another of your liking;
C - dark red (to match the logo), white and perhaps another of your liking.
7. WORD CONTENT: I have attached an Excel file which shows the estimated word content for each page.
8. FUTURE USE OF DESIGN: I'm planning on building a Wordpress website. Can you please ensure the layout design supports this application.

Target Market(s)

oil and gas companies (small and large)

Industry/Entity Type

Oil And Gas

Font styles to use
Sans Serif

Requirements
Nice to have
• The KOL logo and business name should ideally be next to each other. Also, the logo and name should be part of the background graphics, not above it.

```html
<!DOCTYPE html>
<html lang="en">
<head>
<meta charset="utf-8">
<title>KOL — Oil and Gas Consulting</title>
<link href="https://fonts.googleapis.com/css2?family=Montserrat:wght@400;500;700&family=Oswald:wght@400&display=swap" rel="stylesheet">
<style>
  :root {
    --brand-red: #8f1c1f;
    --nav-ink: #1e2a4c;
    --cream: #f5dcab;
    --charcoal: #333333;
    --white: #ffffff;
    --body-ink: #2b2b2b;
  }
  * { margin: 0; padding: 0; box-sizing: border-box; }
  html, body { width: 1200px; height: 667px; overflow: hidden; }
  body {
    position: relative;
    font-family: "Montserrat", Arial, sans-serif;
    background: var(--white);
  }
  .hero-scene {
    position: absolute; inset: 0;
    background: linear-gradient(180deg,
      #a9b8c8 0px, #b7c3b8 14px,
      #e9b24c 100px, #f2c15c 150px, #eba446 220px,
      #c7772f 280px, #6b3b1f 340px, #3c2a1f 385px,
      #8a8478 405px, #c8c2b6 450px, #b6b8bb 520px, #a8adb3 600px,
      #8e96a0 667px);
  }
  .site-header {
    position: absolute; left: 0; top: 15px; width: 1200px; height: 82px;
    background: var(--white);
  }
  .brand {
    position: absolute; left: 158px; top: 16px;
    display: flex; align-items: center; gap: 10px;
    font-weight: 700; font-size: 44px; line-height: 50px;
    color: var(--brand-red); letter-spacing: 1px;
  }
  .brand-mark { width: 16px; height: 16px; background: var(--brand-red); }
  .main-nav {
    position: absolute; right: 158px; top: 25px;
    display: flex; gap: 0; list-style: none;
  }
  .main-nav li {
    font-size: 16px; font-weight: 500; color: var(--nav-ink);
    padding: 6px 10px; height: 31px; line-height: 19px; margin-left: 0;
  }
  .main-nav li.is-active {
    background: var(--brand-red); color: var(--white); border-radius: 3px;
    margin-right: 3px;
  }
  .headline {
    position: absolute; left: 158px; top: 402px; width: 884px; height: 46px;
    background: var(--white);
    font-family: "Oswald", Arial, sans-serif; font-size: 29px; line-height: 46px;
    text-align: center; color: var(--brand-red); letter-spacing: 0;
  }
  .feature {
    position: absolute; top: 457px; width: 288px; height: 126px;
    padding: 28px 16px 0 17px;
    font-size: 12.4px; font-weight: 700; line-height: 18px;
  }
  .feature .more { text-transform: uppercase; }
  .feature--red { left: 158px; background: var(--brand-red); color: var(--white); }
  .feature--cream { left: 456px; background: var(--cream); color: var(--body-ink); font-weight: 500; padding-left: 24px; }
  .feature--cream .more { color: var(--brand-red); }
  .feature--dark { left: 755px; background: var(--charcoal); color: var(--white); padding-left: 20px; }
  .feature--dark .more { color: var(--brand-red); }
  .site-footer {
    position: absolute; left: 0; top: 598px; width: 1200px; height: 60px;
    background: var(--white);
  }
  .copyright {
    position: absolute; left: 158px; top: 23px;
    font-size: 11px; color: var(--brand-red);
  }
  .footer-nav {
    position: absolute; right: 158px; top: 23px;
    display: flex; gap: 15px; list-style: none;
    font-size: 11px; font-weight: 500; color: var(--body-ink);
  }
</style>
</head>
<body>
  <div class="hero-scene" role="img" aria-label="Oil refinery with lit towers at sunset, reflected in calm water"></div>

  <header class="site-header">
    <div class="brand"><span>KOL</span><span class="brand-mark"></span></div>
    <ul class="main-nav">
      <li class="is-active">Home</li>
      <li>About</li>
      <li>Advisory</li>
      <li>Agency</li>
      <li>Investment</li>
      <li>Contact</li>
    </ul>
  </header>

  <h1 class="headline">BEST OIL AND GAS CONSULTING COMPANY IN WORLD</h1>

  <section class="feature feature--red">Lorem ipsum dolor sit amet, consectetur adipisicing elit, sed do eiusmod tempor incididunt ut labore et dolore magna aliqua. Ut enim ad minim...<span class="more">Read more</span></section>
  <section class="feature feature--cream">Lorem ipsum dolor sit amet, consectetur adipisicing elit, sed do eiusmod tempor incididunt ut labore et dolore magna aliqua. Ut enim ad minim...<span class="more">Read more</span></section>
  <section class="feature feature--dark">Lorem ipsum dolor sit amet, consectetur adipisicing elit, sed do eiusmod tempor incididunt ut labore et dolore magna aliqua. Ut enim ad minim...<span class="more">Read more</span></section>

  <footer class="site-footer">
    <p class="copyright">© KOL 2013</p>
    <ul class="footer-nav">
      <li>Home</li><li>About</li><li>Advisory</li><li>Agency</li><li>Investment</li><li>Contact</li>
    </ul>
  </footer>
</body>
</html>
```